PowerPoint Template - Multiple Slide Backgrounds

Looking for a professional PowerPoint template for a technology company. You will see with the logo there's sort of a theme with gears and a lightbulb of sorts. Keeping with this sort of design could help with the brand.

Branding information
• Logo with transparent background included
• Primary Color (Orange) Hex #E6753D
• Secondary Color (Brown) Hex #6A4238
• Primary Font - Myriad Pro
• Secondary Font - Quiet Sans Light

Design request -
• PowerPoint (POTX) template with master slide views
• Cover Slide
• Color Pallet - 7 Color PowerPoint pallet that includes and complements primary and secondary colors
• Slide Master with Footer
• Multiple Background Types to allow for smart art overlay or bullet point text boxes
Bonus - Sample graphical elements using shapes and smart art

```html
<!DOCTYPE html>
<html lang="en">
<head>
<meta charset="utf-8">
<title>Ridgeline Ops - Third Part</title>
<link rel="stylesheet" href="https://fonts.googleapis.com/css2?family=Source+Sans+3:wght@400;600;700&display=swap">
<style>
  :root {
    --brown: #6a4238;
    --orange: #e6753d;
    --peach: #f2a97a;
    --peach-soft: #f9dccb;
    --charcoal: #3b3b3b;
    --coral: #ec5d57;
    --navy: #053d7c;
    --footer: #5a5a5a;
    --ring-grey: #d9d9d9;
    --canvas: #ebebeb;
    --text: #444;
    --caption: #1d5a8a;
  }
  * { margin: 0; padding: 0; box-sizing: border-box; }
  html, body { width: 1200px; height: 1050px; overflow: hidden; }
  body { background: var(--canvas); font-family: "Source Sans 3", "Myriad Pro", sans-serif; position: relative; }

  .slide { position: absolute; width: 556px; height: 313px; background: #fff; overflow: hidden; }
  .slide--concept { left: 21px; top: 13px; }
  .slide--team { left: 618px; top: 13px; }
  .slide--closing { left: 21px; top: 335px; width: 557px; height: 314px; }
  .slide--palette { left: 618px; top: 335px; }

  .slide__title { position: absolute; left: 17px; top: 19px; font-size: 22px; font-weight: 700; color: var(--brown); letter-spacing: -0.2px; }
  .slide__title::after { content: ""; position: absolute; left: 0; top: 32px; width: 71px; height: 1.5px; background: var(--orange); }

  .brand { position: absolute; right: 18px; top: 28px; display: flex; align-items: center; gap: 3px; font-size: 7px; font-weight: 700; color: var(--brown); }
  .brand__dot { width: 9px; height: 9px; border-radius: 50%; background: var(--orange); }

  .footer { position: absolute; left: 0; bottom: 0; width: 100%; height: 17px; background: var(--footer); }
  .footer__label { position: absolute; left: 17px; top: 5px; font-size: 6px; font-weight: 700; color: #fff; }
  .footer__page { position: absolute; right: 0; bottom: 0; width: 38px; height: 25px; background: var(--brown); clip-path: polygon(22% 0, 100% 0, 100% 100%, 0 100%); color: #fff; font-size: 7px; font-weight: 700; display: flex; align-items: center; justify-content: center; padding-left: 6px; }

  .note { position: absolute; width: 90px; text-align: center; font-size: 8px; line-height: 1.35; color: var(--text); }

  .concept-art { position: absolute; left: 0; top: 0; }

  .member { position: absolute; display: flex; align-items: center; gap: 14px; }
  .member__photo { width: 78px; height: 78px; border-radius: 50%; border: 4px solid var(--brown); padding: 3px; background: #fff; }
  .member__photo span { display: block; width: 100%; height: 100%; border-radius: 50%; background: radial-gradient(circle at 50% 40%, #c9a48d, #8a6d5e 70%, #5b4a42); }
  .member__name { font-size: 12px; font-weight: 700; color: var(--orange); margin-bottom: 3px; }
  .member__bio { font-size: 8px; line-height: 1.35; color: var(--text); }

  .closing-art { position: absolute; left: 0; top: 0; }
  .closing__title { position: absolute; left: 29px; top: 128px; font-size: 35px; font-weight: 700; color: var(--brown); letter-spacing: -0.8px; }
  .closing__rule { position: absolute; left: 29px; top: 180px; width: 131px; height: 1.5px; background: var(--orange); }
  .closing .brand { left: 30px; right: auto; top: auto; bottom: 24px; }

  .palette-bar { position: absolute; left: 18px; top: 139px; width: 521px; height: 50px; display: flex; }
  .palette-bar span { height: 100%; }
  .palette-label { position: absolute; font-size: 8px; color: var(--text); }

  .caption { position: absolute; left: 18px; top: 990px; font-family: Arial, "Source Sans 3", sans-serif; font-size: 44px; font-weight: 700; color: var(--caption); }
</style>
</head>
<body>

<section class="slide slide--concept">
  <h2 class="slide__title">Concept Slide</h2>
  <div class="brand"><span class="brand__dot"></span>Ridgeline Ops</div>

  <svg class="concept-art" width="556" height="313" viewBox="0 0 556 313">
    <g fill="none" stroke-width="9">
      <path d="M58 173 A52 52 0 0 1 162 173" stroke="var(--brown)"/>
      <path d="M58 173 A52 52 0 0 0 162 173" stroke="var(--ring-grey)"/>
      <path d="M169 173 A52 52 0 0 1 273 173" stroke="var(--ring-grey)"/>
      <path d="M169 173 A52 52 0 0 0 273 173" stroke="var(--brown)"/>
      <path d="M280 173 A52 52 0 0 1 384 173" stroke="var(--brown)"/>
      <path d="M280 173 A52 52 0 0 0 384 173" stroke="var(--ring-grey)"/>
      <path d="M391 173 A52 52 0 0 1 495 173" stroke="var(--ring-grey)"/>
      <path d="M391 173 A52 52 0 0 0 495 173" stroke="var(--brown)"/>
    </g>
    <g fill="var(--orange)">
      <path d="M109 157 A18 18 0 1 0 128 175 L109 175 Z"/>
      <path d="M112 154 A18 18 0 0 1 131 172 L112 172 Z"/>
      <path d="M207 157 h16 l6 6 v24 h-22 Z"/>
      <circle cx="231" cy="181" r="7" fill="#fff" stroke="var(--orange)" stroke-width="3"/>
      <path d="M235 186 l7 7" stroke="var(--orange)" stroke-width="3"/>
      <circle cx="332" cy="161" r="7"/>
      <path d="M316 191 q0-16 16-16 q16 0 16 16 Z"/>
      <path d="M423 170 l10-7 l10 5 l10-5 l10 7 l-14 14 q-4 4-8 0 Z"/>
    </g>
  </svg>

  <p class="note" style="left:176px;top:79px;">Lorem ipsum dolor sit amet</p>
  <p class="note" style="left:402px;top:79px;">Lorem ipsum dolor sit amet</p>
  <p class="note" style="left:64px;top:249px;">Lorem ipsum dolor sit amet</p>
  <p class="note" style="left:289px;top:249px;">Lorem ipsum dolor sit amet</p>

  <footer class="footer"><span class="footer__label">Footer</span></footer>
  <div class="footer__page">13</div>
</section>

<section class="slide slide--team">
  <h2 class="slide__title">Team</h2>
  <div class="brand"><span class="brand__dot"></span>Ridgeline Ops</div>

  <div class="member" style="left:35px;top:83px;">
    <div class="member__photo"><span role="img" aria-label="Team member portrait"></span></div>
    <div><p class="member__name">Name</p><p class="member__bio">Lorem ipsum dolor sit amet,<br>consectetur adipiscing elit.</p></div>
  </div>
  <div class="member" style="left:315px;top:83px;">
    <div class="member__photo"><span role="img" aria-label="Team member portrait"></span></div>
    <div><p class="member__name">Name</p><p class="member__bio">Lorem ipsum dolor sit amet,<br>consectetur adipiscing elit.</p></div>
  </div>
  <div class="member" style="left:35px;top:187px;">
    <div class="member__photo"><span role="img" aria-label="Team member portrait"></span></div>
    <div><p class="member__name">Name</p><p class="member__bio">Lorem ipsum dolor sit amet,<br>consectetur adipiscing elit.</p></div>
  </div>
  <div class="member" style="left:315px;top:187px;">
    <div class="member__photo"><span role="img" aria-label="Team member portrait"></span></div>
    <div><p class="member__name">Name</p><p class="member__bio">Lorem ipsum dolor sit amet,<br>consectetur adipiscing elit.</p></div>
  </div>

  <footer class="footer"><span class="footer__label">Footer</span></footer>
  <div class="footer__page">14</div>
</section>

<section class="slide slide--closing closing">
  <svg class="closing-art" width="557" height="314" viewBox="0 0 557 314">
    <defs>
      <radialGradient id="techGlow" cx="0.75" cy="0.35" r="0.7">
        <stop offset="0" stop-color="#3a5f7a"/>
        <stop offset="0.5" stop-color="#1b3248"/>
        <stop offset="1" stop-color="#0d1b2a"/>
      </radialGradient>
    </defs>
    <rect x="250" y="0" width="307" height="314" fill="url(#techGlow)" role="img" aria-label="Photo of a hand touching a glowing digital network"/>
    <circle cx="-25" cy="165" r="385" fill="var(--brown)"/>
    <circle cx="-40" cy="165" r="365" fill="#fff"/>
    <circle cx="-45" cy="190" r="378" fill="var(--peach-soft)"/>
    <circle cx="-60" cy="190" r="365" fill="#fff"/>
  </svg>
  <h2 class="closing__title">THANK YOU!</h2>
  <div class="closing__rule"></div>
  <div class="brand"><span class="brand__dot"></span>Ridgeline Ops</div>
</section>

<section class="slide slide--palette">
  <h2 class="slide__title">Color Pallet</h2>
  <div class="brand"><span class="brand__dot"></span>Ridgeline Ops</div>

  <p class="palette-label" style="left:344px;top:115px;">Secondary</p>
  <div class="palette-bar">
    <span style="width:155px;background:var(--brown);"></span>
    <span style="width:111px;background:var(--orange);"></span>
    <span style="width:78px;background:var(--peach);"></span>
    <span style="width:65px;background:var(--charcoal);"></span>
    <span style="width:56px;background:var(--coral);"></span>
    <span style="width:56px;background:var(--navy);"></span>
  </div>
  <p class="palette-label" style="left:158px;top:209px;">Primary</p>
  <p class="palette-label" style="left:466px;top:209px;">Highlight</p>

  <footer class="footer"><span class="footer__label">Footer</span></footer>
  <div class="footer__page">16</div>
</section>

<h1 class="caption">Ridgeline Ops - Third Part</h1>

</body>
</html>
```